Venture Capital firm needs modern business cards

We are a Venture Capital firm within financial services/Asset management. The industry generally has basic business cards with black, blue and maybe green/yellow design elements.
Our firm has a four-colour swoosh logo. We are based in London and want to stand out, just a little bit!, from the crowd. Our company is called ROLK Investments and the 'C' stands for collaboration thus using artfolkhub is a natural portal for our business card design competition. Our logo came via artfolkhub too!
We use 'Venture Partner in Asset Management' as our tagline and this is Trademark registered. We operate in a conservative industry and we should not overstep our mark. The logo is colorful as it is and therefore the rest of the design should not be too fanciful.
The objective is twofold: make our logo element stick and memorable with our audience, whilst representing a conservative yet young image.
The Business Card obviously needs a field for Name, Surname, Job Title, Adress fields: Street, City, Postcode, Country, telefone and cell number, website address, etc.
We have uploaded the ai file. We trust that these are OK. If not, please advise.
Reason: We have have been busy with a client engagement. We will set the project as Guaranteed in return for the troubles we cause. Apologies for the confusion.
Thank you all for these great and creative design suggestions. The team is very happy with a number of your ideas! We will be in touch tomorrow to give individual feedback before the project closes on Friday. We look forward to working with some of you to narrow down your creations. Thank you, ROLK Investments team.
All,
Target Market(s)
Financial Services Professionals, Investors, Media, 35-70 years, mainly male, well educated
Industry/Entity Type
Conservative
Requirements
Must have
- We must make use of our logo and potential tagline 'Venture Partner in Asset Management' as we are establishing a new Brand and new company in the market.
We can use 'ROLK', 'ROLK Investments', and 'ROLK Investments'+tagline 'Venture Partner in Asset Management' or simply the four-colour swoosh plus the name of the company as part of the text. (see files)
All design elements are available in black or grey-scale if required. (grey scale swoosh attached).
Due to regulation we must have the following wording on the card in small print 'ROLK Investments is an Appointed Representative of Brambury Monetary Ventures Limited, which is authorised by the Pemberton Oversight Board'.
Nice to have
- We would consider designs that make use of different printing techniques such embossing/debossing, UV spot etc.
We attach our colour palette in the files section for your reference.
Should not have
- The font we use for our company name is 'EXO' so do not use a font style that clashes with the corporate fonts, please.
Do not use other design elements than the ones we provide in the file library as part of this project.

```html
<!DOCTYPE html>
<html lang="en">
<head>
<meta charset="utf-8">
<title>ROLK Investments – Business Card</title>
<link href="https://fonts.googleapis.com/css2?family=Barlow:wght@300;400&display=swap" rel="stylesheet">
<style>
  :root {
    --stage: #9b9b9b;
    --card: #ffffff;
    --ink-grey: #8a8a8a;
    --ink-light: #a3a3a3;
    --accent-green: #8cc63f;
    --mark-grey: #5f5f5f;
  }
  * { margin: 0; padding: 0; box-sizing: border-box; }
  html, body {
    width: 1200px;
    height: 487px;
    overflow: hidden;
  }
  body {
    background: var(--stage);
    font-family: "Barlow", sans-serif;
    font-weight: 300;
    position: relative;
  }
  .card {
    position: absolute;
    top: 79px;
    width: 532px;
    height: 327px;
    background: var(--card);
  }
  .card--front { left: 53px; }
  .card--back { left: 607px; }

  .holder {
    position: absolute;
    left: 137px;
    top: 26px;
  }
  .holder__name {
    font-size: 19px;
    font-weight: 400;
    color: var(--ink-grey);
    line-height: 1.1;
  }
  .holder__title {
    font-size: 14px;
    font-weight: 400;
    color: var(--accent-green);
    margin-top: 3px;
  }

  .brand__dot {
    position: absolute;
    left: 24px;
    top: 98px;
    width: 84px;
    height: 84px;
    border-radius: 50%;
    background: var(--accent-green);
  }
  .brand__text {
    position: absolute;
    left: 135px;
    top: 90px;
  }
  .brand__name {
    font-size: 74px;
    font-weight: 400;
    color: var(--mark-grey);
    line-height: 0.95;
  }
  .brand__sub {
    font-size: 16px;
    font-weight: 400;
    letter-spacing: 7.2px;
    color: var(--mark-grey);
    line-height: 1.2;
    margin-top: 4px;
  }
  .brand__tagline {
    font-size: 10px;
    font-weight: 400;
    color: var(--accent-green);
    letter-spacing: 0.3px;
    margin-top: 3px;
  }

  .contact {
    position: absolute;
    left: 137px;
    top: 244px;
    font-size: 13.5px;
    color: var(--ink-grey);
    line-height: 18px;
  }
  .contact__label {
    color: var(--accent-green);
    font-weight: 400;
    margin-right: 8px;
  }
  .contact__gap { margin-left: 12px; }

  .back-brand {
    position: absolute;
    left: 143px;
    top: 141px;
    display: flex;
    align-items: center;
    gap: 16px;
  }
  .back-brand__dot {
    width: 48px;
    height: 48px;
    border-radius: 50%;
    background: var(--accent-green);
  }
  .back-brand__url {
    font-size: 14.5px;
    color: var(--ink-grey);
  }
  .back-brand__url strong {
    font-weight: 400;
    color: var(--accent-green);
  }
  .regulatory {
    position: absolute;
    left: 40px;
    right: 40px;
    bottom: 18px;
    font-size: 8px;
    line-height: 1.35;
    text-align: center;
    color: var(--ink-light);
  }
</style>
</head>
<body>
  <section class="card card--front">
    <div class="holder">
      <p class="holder__name">CARDHOLDER NAME</p>
      <p class="holder__title">Designation</p>
    </div>

    <span class="brand__dot"></span>
    <div class="brand__text">
      <p class="brand__name">ROLK</p>
      <p class="brand__sub">Investments</p>
      <p class="brand__tagline">Venture Partner in Asset Management</p>
    </div>

    <div class="contact">
      <p>0101 Sunset Avenue, Suite No. 123,</p>
      <p>Your City, City Code, Your Country</p>
      <p><span class="contact__label">t</span>+012 345 6789<span class="contact__label contact__gap">f</span>+012 345 6780</p>
      <p><span class="contact__label">e</span>cardholder.name@rolkinvestments.com</p>
    </div>
  </section>

  <section class="card card--back">
    <div class="back-brand">
      <span class="back-brand__dot"></span>
      <span class="back-brand__url">www.<strong>rolkinvestments</strong>.com</span>
    </div>
    <p class="regulatory">ROLK Investments is an Appointed Representative of Brambury Monetary Ventures Limited, which is authorised by the Pemberton Oversight Board</p>
  </section>
</body>
</html>
```